Veltrano - Mechanic/Collision Center Business Card

We're looking for a business card design for our mechanic/ collision repair shop.

Can be with colours or monochromatic.

See the attached files.

Many thanks

```html
<!DOCTYPE html>
<html lang="pt">
<head>
<meta charset="utf-8">
<title>Veltrano – Business Card</title>
<link rel="stylesheet" href="https://fonts.googleapis.com/css2?family=Montserrat:wght@400;500;700;800&display=swap">
<style>
  :root {
    --teal: #2a93a8;
    --teal-dark: #14637a;
    --teal-light: #46aabb;
    --ink: #2b2b2b;
    --grey: #6f6f6f;
    --stripe-grey: #8c8c8e;
    --paper: #fbfbfb;
    --backdrop: #e6e8ea;
  }
  * { box-sizing: border-box; margin: 0; padding: 0; }
  html, body {
    width: 1200px; height: 900px; overflow: hidden;
    background: var(--backdrop);
    font-family: "Montserrat", sans-serif;
  }
  .sheet {
    width: 1200px; height: 900px;
    display: flex; flex-direction: column; align-items: center; justify-content: center;
    gap: 40px;
  }
  .card {
    position: relative;
    width: 700px; height: 400px;
    overflow: hidden;
    box-shadow: 0 6px 18px rgba(0,0,0,.15);
  }

  /* Front */
  .card-front { background: var(--paper); }
  .brand {
    position: absolute; left: 40px; top: 92px;
    display: flex; align-items: center; gap: 12px;
  }
  .brand-dot { width: 22px; height: 22px; border-radius: 50%; background: var(--teal); }
  .brand-name {
    font-weight: 800; font-size: 40px; color: var(--ink); letter-spacing: 1px;
  }
  .brand-rule {
    position: absolute; left: 40px; top: 180px; width: 330px; height: 2px;
    background: var(--grey);
  }
  .contact-block {
    position: absolute; right: 40px; top: 38px; text-align: right;
    width: 300px;
  }
  .company { font-weight: 700; font-size: 20px; color: var(--teal); letter-spacing: 1px; }
  .line { font-size: 14px; color: var(--grey); letter-spacing: .5px; }
  .person { font-weight: 700; font-size: 20px; color: var(--teal); letter-spacing: 1px; margin-top: 8px; }
  .contact-rule { height: 2px; background: var(--grey); margin-top: 6px; }
  .details {
    position: absolute; left: 220px; top: 180px; width: 300px; text-align: center;
    color: var(--ink);
  }
  .details dt { font-weight: 700; font-size: 15px; }
  .details dd { font-size: 14px; margin-bottom: 10px; letter-spacing: .3px; }
  .band { position: absolute; left: 0; bottom: 0; width: 700px; height: 120px; }

  /* Back */
  .card-back {
    background: linear-gradient(135deg, var(--teal-light) 0%, var(--teal) 45%, var(--teal-dark) 100%);
    color: #fff;
  }
  .back-brand {
    position: absolute; left: 0; right: 0; top: 130px;
    display: flex; align-items: center; justify-content: center; gap: 18px;
  }
  .back-dot { width: 34px; height: 34px; border-radius: 50%; background: #fff; }
  .back-name { font-weight: 800; font-size: 76px; letter-spacing: 2px; }
  .back-rule {
    position: absolute; left: 110px; top: 245px; width: 480px; height: 3px; background: #fff;
  }
  .web {
    position: absolute; right: 70px; bottom: 60px;
    font-weight: 500; font-size: 20px; letter-spacing: .5px;
  }
</style>
</head>
<body>
<main class="sheet">

  <section class="card card-front" aria-label="Front of card">
    <div class="brand">
      <span class="brand-dot"></span>
      <span class="brand-name">VELTRANO</span>
    </div>
    <div class="brand-rule"></div>

    <div class="contact-block">
      <p class="company">VELTRANO, LDA</p>
      <p class="line">Phone: +351 214 550 730</p>
      <p class="person">RUI MATOS</p>
      <p class="line">Manager</p>
      <p class="line">Phone: +351 912 408 615</p>
      <div class="contact-rule"></div>
    </div>

    <dl class="details">
      <dt>Address</dt>
      <dd>Rua das Oficinas, 42</dd>
      <dt>Postal code</dt>
      <dd>1900-310 Lisboa</dd>
      <dt>Email</dt>
      <dd>geral@veltrano.pt</dd>
    </dl>

    <svg class="band" viewBox="0 0 700 120" aria-hidden="true">
      <polygon points="0,104 400,104 430,50 700,50 700,120 0,120" fill="var(--teal)"/>
      <polygon points="0,78 18,78 8,96 0,96" fill="var(--teal)"/>
      <polygon points="40,78 120,78 110,96 30,96" fill="var(--stripe-grey)"/>
      <polygon points="150,78 230,78 220,96 140,96" fill="var(--teal)"/>
      <polygon points="260,78 340,78 330,96 250,96" fill="var(--stripe-grey)"/>
      <polygon points="370,56 420,56 398,96 340,96" fill="var(--stripe-grey)" opacity=".0"/>
    </svg>
  </section>

  <section class="card card-back" aria-label="Back of card">
    <div class="back-brand">
      <span class="back-dot"></span>
      <span class="back-name">VELTRANO</span>
    </div>
    <div class="back-rule"></div>
    <p class="web">www.veltrano.pt</p>
  </section>

</main>
</body>
</html>
```